Corvid Lens Studio Business Card Design

I need a business card designed for a photography business based in Perth, Western Australia called Corvid Lens Studio.

We specialise in wedding, event photography and portrait photography.

The business card must borrow the style of the attached logo.

The hex codes for the colours in the logo are:
#ED1D85 - Pink
#89C23E - Green
#37282F - Black

The name on the card will be:
Name: Tobiah
Phone: 0417395268
Website: www.corvidlensstudio.com.au
Facebook: corvidlensstudio

I am open and happy to accept creative concepts.

Industry/Entity Type

Business

```html
<!DOCTYPE html>
<html lang="en">
<head>
<meta charset="utf-8">
<title>Corvid Lens Studio – Business Card</title>
<link rel="stylesheet" href="https://fonts.googleapis.com/css2?family=Lato:wght@300;400;700&display=swap">
<style>
  :root {
    --stage: #3a3a3a;
    --card: #050505;
    --pink: #ED1D85;
    --green: #89C23E;
    --ink: #37282F;
    --text-muted: #5e5358;
    --text-name: #6f6368;
  }
  * { box-sizing: border-box; margin: 0; padding: 0; }
  html, body {
    width: 1200px;
    height: 926px;
    overflow: hidden;
    background: var(--stage);
    font-family: "Lato", Arial, sans-serif;
  }
  .stage {
    position: relative;
    width: 1200px;
    height: 926px;
    display: flex;
    flex-direction: column;
    align-items: center;
    justify-content: center;
    gap: 48px;
  }
  .card {
    width: 700px;
    height: 400px;
    background: var(--card);
    display: flex;
    flex-direction: column;
    align-items: center;
    justify-content: center;
    box-shadow: 0 10px 30px rgba(0,0,0,0.35);
  }
  .brand {
    display: flex;
    flex-direction: column;
    align-items: center;
  }
  .brand-dot {
    width: 64px;
    height: 64px;
    border-radius: 50%;
    background: var(--pink);
    margin-bottom: 22px;
  }
  .brand-name {
    font-weight: 300;
    font-size: 15px;
    letter-spacing: 0.62em;
    text-transform: uppercase;
    color: var(--text-muted);
    padding-left: 0.62em;
  }
  .card--back .brand-dot { width: 74px; height: 74px; margin-bottom: 26px; }
  .card--back .brand-name { font-size: 17px; }

  .card--front { justify-content: flex-start; padding-top: 62px; }
  .card--front .brand-dot { width: 50px; height: 50px; margin-bottom: 16px; }
  .card--front .brand-name { font-size: 11px; }
  .holder-name {
    margin-top: 26px;
    font-weight: 400;
    font-size: 34px;
    letter-spacing: 0.06em;
    text-transform: uppercase;
    color: var(--text-name);
  }
  .divider {
    width: 110px;
    height: 2px;
    background: var(--green);
    margin: 6px 0 12px;
  }
  .contact {
    list-style: none;
    text-align: center;
    font-size: 17px;
    line-height: 1.32;
    color: var(--text-muted);
  }
  .contact-label { font-weight: 700; }
</style>
</head>
<body>
  <main class="stage">
    <section class="card card--back" aria-label="Card back">
      <div class="brand">
        <span class="brand-dot"></span>
        <span class="brand-name">Corvid Lens Studio</span>
      </div>
    </section>

    <section class="card card--front" aria-label="Card front">
      <div class="brand">
        <span class="brand-dot"></span>
        <span class="brand-name">Corvid Lens Studio</span>
      </div>
      <h1 class="holder-name">Tobiah</h1>
      <div class="divider"></div>
      <ul class="contact">
        <li><span class="contact-label">Phone:</span> 0417395268</li>
        <li><span class="contact-label">Web:</span> www.corvidlensstudio.com.au</li>
        <li><span class="contact-label">Facebook:</span> corvidlensstudio</li>
      </ul>
    </section>
  </main>
</body>
</html>
```